Heronvale Yards LLC - Door Hanger for Residential Mowing

Door Hanger- Heronvale Yards LLC. I would like the Heronvale Logo on a white background with three shades of pink incorporated into the flyer. Our phone number is 904-382-7046. And our website is heronvaleyardworks-example.com. I would like for the door hanger to mirror the Copperbend Door Hanger, using the Heronvale logo & information.

List of Services to include:
Pest Control
Termite Inspection
Lawn Maintenance
Debris Clean-up
Trash Removal
Home Inspection
Handy-man Services

Target Market(s)

Residential Lawns

Industry/Entity Type

Lawn Care

Font styles to use
Sans Serif

Colors
e34197
e667a6
eea4c8
f9d9e8

Requirements
Must have
• Phone Number
• Must be a Door Hanger
• Website
• 2 Sided
Nice to have
• 3 Shades of Pink with white background
Should not have
• It must be a door hanger. KEEP IN MIND THERE WILL BE A PUNCH HOLE AT TOP.......

```html
<!DOCTYPE html>
<html lang="en">
<head>
<meta charset="utf-8">
<title>Heronvale Yards LLC – Door Hanger</title>
<link rel="stylesheet" href="https://fonts.googleapis.com/css2?family=Anton&family=Open+Sans:wght@400;600&display=swap">
<style>
  :root {
    --pink-deep: #e34197;
    --pink-mid: #e667a6;
    --pink-soft: #eea4c8;
    --pink-pale: #f9d9e8;
    --ink: #161616;
    --white: #ffffff;
    --stage: #ececec;
    --grass: #5f9a2e;
    --smoke: #c9ced4;
  }
  * { box-sizing: border-box; margin: 0; padding: 0; }
  html, body { width: 1200px; height: 819px; overflow: hidden; }
  body { background: var(--stage); font-family: "Open Sans", sans-serif; position: relative; }

  .hanger {
    position: absolute; top: 24px; width: 380px; height: 770px;
    background: var(--white); overflow: hidden;
    box-shadow: 0 4px 14px rgba(0,0,0,.18);
  }
  .hanger--front { left: 190px; }
  .hanger--back { left: 630px; background: linear-gradient(180deg, var(--white) 8%, var(--pink-pale) 45%, var(--pink-soft) 75%, var(--pink-mid) 92%); }

  .brand { position: absolute; display: flex; align-items: center; gap: 8px; }
  .brand__dot { border-radius: 50%; background: var(--pink-deep); flex: none; }
  .brand__text { color: var(--pink-deep); font-weight: 400; line-height: 1; }
  .brand__name { display: block; }
  .brand__tag { display: block; letter-spacing: .3em; margin-top: 4px; }
  .hanger--front .brand { top: 44px; right: 22px; }
  .hanger--front .brand__dot { width: 30px; height: 30px; }
  .hanger--front .brand__name { font-size: 34px; }
  .hanger--front .brand__tag { font-size: 11px; }
  .hanger--back .brand { top: 40px; right: 22px; }
  .hanger--back .brand__dot { width: 18px; height: 18px; }
  .hanger--back .brand__name { font-size: 20px; }
  .hanger--back .brand__tag { font-size: 7px; }

  .front-art { position: absolute; inset: 0; }

  .headline { position: absolute; left: 22px; top: 118px; font-family: "Anton", sans-serif; font-weight: 400; color: var(--pink-deep); text-shadow: 2px 2px 0 #2a0a1a; }
  .headline__main { font-size: 48px; line-height: 1.05; display: block; }
  .headline__sub { font-size: 20px; line-height: 1.2; display: block; margin-top: 4px; letter-spacing: .2px; }

  .cta { position: absolute; left: 0; right: 0; bottom: 0; height: 170px; color: var(--white); }
  .cta__tab { position: absolute; left: 24px; top: 26px; background: var(--pink-deep); font-size: 15px; padding: 4px 12px; border-radius: 3px 0 0 3px; width: 250px; }
  .cta__phone { position: absolute; left: 24px; top: 62px; font-family: "Anton", sans-serif; font-size: 44px; line-height: 1.2; letter-spacing: .5px; }
  .cta__more { position: absolute; left: 24px; top: 126px; font-size: 12px; }
  .cta__web { position: absolute; left: 24px; top: 142px; font-size: 14px; color: var(--pink-mid); }

  .services__title { position: absolute; left: 24px; top: 66px; font-family: "Anton", sans-serif; font-weight: 400; font-size: 28px; color: var(--pink-deep); text-shadow: 1px 1px 0 #2a0a1a; }
  .service { position: absolute; width: 116px; text-align: center; }
  .service__photo { width: 116px; height: 100px; border-radius: 16px; border: 2px solid var(--pink-deep); box-shadow: 0 2px 6px rgba(0,0,0,.2); }
  .service__label { font-family: "Anton", sans-serif; font-size: 15px; line-height: 1.3; color: var(--pink-deep); text-shadow: 1px 1px 0 #2a0a1a; margin-top: 5px; white-space: nowrap; margin-left: -20px; margin-right: -20px; }
  .photo--pest { background: radial-gradient(circle at 40% 60%, #e8eaed, var(--smoke) 50%, #6c8a58); }
  .photo--termite { background: linear-gradient(135deg, #cfc7b8, #8b6a4e); }
  .photo--lawn { background: linear-gradient(180deg, #7ab540, var(--grass) 60%, #c9302c 61%, #c9302c 75%, var(--grass) 76%); }
  .photo--debris { background: linear-gradient(160deg, #4e6b3a, #8ba26a 60%, #d8d4cc); }
  .photo--trash { background: linear-gradient(180deg, #cbbf9f 30%, #6f6a66 60%, #5d8a37); }
  .photo--inspect { background: radial-gradient(circle at 55% 45%, #9aa3ad 30%, #c9c2b3 55%, #77a148); }
  .photo--handy { background: radial-gradient(circle at 50% 60%, #e9e9e9 30%, #c7cfd8 60%, #6b4a32); }

  .footer { position: absolute; left: 0; right: 0; bottom: 0; height: 64px; background: var(--ink); border-top: 4px solid var(--white); color: var(--white); text-align: center; font-size: 13px; }
  .footer__row { display: flex; justify-content: center; align-items: center; gap: 8px; margin-top: 12px; }
  .footer__row svg { width: 14px; height: 14px; fill: var(--white); }
  .footer__sep { margin: 0 6px; }
  .footer__web { color: var(--pink-mid); margin-top: 5px; }
</style>
</head>
<body>

<section class="hanger hanger--front">
  <svg class="front-art" width="380" height="770" viewBox="0 0 380 770">
    <path d="M0,235 C140,200 300,235 380,330 L380,430 C330,320 170,260 0,280 Z" fill="var(--pink-deep)"/>
    <path d="M0,280 C170,260 330,320 380,430 L380,470 C320,350 160,295 0,310 Z" fill="var(--pink-mid)"/>
    <path d="M0,310 C160,295 320,350 380,470 L380,500 C310,380 160,330 0,338 Z" fill="var(--pink-soft)"/>
    <path d="M160,630 C260,560 350,490 380,420" stroke="var(--pink-soft)" stroke-width="14" fill="none"/>
    <path d="M180,640 C280,575 360,500 380,460" stroke="var(--ink)" stroke-width="6" fill="none"/>
    <g role="img" aria-label="Photo of a two-storey house seen through a magnifying glass">
      <circle cx="110" cy="345" r="95" fill="#cfd6dc" stroke="var(--pink-deep)" stroke-width="6"/>
    </g>
    <g role="img" aria-label="Photo of a technician fogging a yard for pest control">
      <circle cx="290" cy="425" r="90" fill="var(--smoke)" stroke="var(--pink-deep)" stroke-width="7"/>
    </g>
    <g role="img" aria-label="Photo of a lawn mower on green grass">
      <circle cx="105" cy="530" r="110" fill="var(--grass)" stroke="var(--pink-deep)" stroke-width="8"/>
    </g>
    <path d="M0,610 C120,580 260,610 380,700 L380,770 L0,770 Z" fill="var(--ink)"/>
    <path d="M0,600 C120,572 260,600 380,690 L380,700 C260,610 120,580 0,610 Z" fill="var(--pink-deep)"/>
  </svg>

  <div class="brand">
    <span class="brand__dot"></span>
    <span class="brand__text"><span class="brand__name">Heronvale</span><span class="brand__tag">HOME SERVICES</span></span>
  </div>

  <h1 class="headline">
    <span class="headline__main">now offering</span>
    <span class="headline__sub">Home Services in your neighborhood</span>
  </h1>

  <div class="cta">
    <div class="cta__tab">call to schedule service today</div>
    <div class="cta__phone">904-382-7046</div>
    <div class="cta__more">for more info go to</div>
    <div class="cta__web">heronvaleyardworks-example.com</div>
  </div>
</section>

<section class="hanger hanger--back">
  <h2 class="services__title">Our Services</h2>
  <div class="brand">
    <span class="brand__dot"></span>
    <span class="brand__text"><span class="brand__name">Heronvale</span><span class="brand__tag">HOME SERVICES</span></span>
  </div>

  <div class="service" style="left:50px;top:118px"><div class="service__photo photo--pest" role="img" aria-label="Pest control fogging photo"></div><div class="service__label">Pest Control</div></div>
  <div class="service" style="left:214px;top:108px"><div class="service__photo photo--termite" role="img" aria-label="Termite inspection photo"></div><div class="service__label">Termite Inspection</div></div>
  <div class="service" style="left:50px;top:258px"><div class="service__photo photo--lawn" role="img" aria-label="Lawn mower on grass photo"></div><div class="service__label">Lawn Maintenance</div></div>
  <div class="service" style="left:214px;top:248px"><div class="service__photo photo--debris" role="img" aria-label="Fallen branches on a driveway photo"></div><div class="service__label">Debris Clean-up</div></div>
  <div class="service" style="left:50px;top:398px"><div class="service__photo photo--trash" role="img" aria-label="Pile of household junk in front of a house photo"></div><div class="service__label">Trash Removal</div></div>
  <div class="service" style="left:214px;top:388px"><div class="service__photo photo--inspect" role="img" aria-label="House under a magnifying glass photo"></div><div class="service__label">Home Inspection</div></div>
  <div class="service" style="left:132px;top:530px"><div class="service__photo photo--handy" role="img" aria-label="Tools arranged around a small house illustration"></div><div class="service__label">Handy-man Services</div></div>

  <footer class="footer">
    <div class="footer__row">
      <svg viewBox="0 0 24 24"><path d="M6.6 10.8a15 15 0 0 0 6.6 6.6l2.2-2.2c.3-.3.7-.4 1-.2 1.1.4 2.3.6 3.6.6.6 0 1 .4 1 1V20c0 .6-.4 1-1 1A17 17 0 0 1 3 4c0-.6.4-1 1-1h3.5c.6 0 1 .4 1 1 0 1.3.2 2.5.6 3.6.1.3 0 .7-.2 1z"/></svg>
      <span>904-382-7046</span>
      <span class="footer__sep">|</span>
      <svg viewBox="0 0 24 24"><path d="M2 5h20v14H2z M2 5l10 8 10-8" fill="none" stroke="#fff" stroke-width="2"/></svg>
      <span>office@heronvale-example.com</span>
    </div>
    <div class="footer__web">heronvaleyardworks-example.com</div>
  </footer>
</section>

</body>
</html>
```